lawn sign

Lawn Sign
Roofing Gutters Windows

Target Market(s)

roofing

Font styles to use
Sans Serif

Colors
86cfc6
33a6d7
fbee3f
faa54b

Requirements
Must have
• my logo
Nice to have
• designer for now

```html
<!DOCTYPE html>
<html lang="en">
<head>
<meta charset="utf-8">
<title>Lawn Sign – Windows, Roofing, Gutters</title>
<link rel="stylesheet" href="https://fonts.googleapis.com/css2?family=Play:wght@400;700&display=swap">
<style>
  :root {
    --paper: #ffffff;
    --ink: #333638;
    --ink-soft: #4a4d50;
    --rule: #e0e2e4;
    --teal: #86cfc6;
    --blue: #33a6d7;
    --yellow: #fbee3f;
    --orange: #faa54b;
    --deep-orange: #f26a21;
    --green: #4fc07a;
    --brand: #4ca86a;
  }
  html, body {
    margin: 0;
    padding: 0;
    width: 1200px;
    height: 850px;
    overflow: hidden;
    background: var(--paper);
  }
  .lawn-sign {
    display: block;
    width: 1200px;
    height: 850px;
    font-family: "Play", sans-serif;
  }
  .guide-line { stroke: var(--rule); stroke-width: 1.2; fill: none; }
  .tile-frame { stroke: var(--paper); stroke-width: 7; }
  .accent-tile { fill: url(#accentGradient); }
  .warranty-figure { font-size: 40px; font-weight: 700; fill: var(--ink); letter-spacing: 1px; }
  .warranty-label { font-size: 19px; fill: var(--ink-soft); letter-spacing: 2.4px; }
  .service-badge { fill: url(#badgeGradient); }
  .service-glyph { fill: var(--paper); }
  .service-label { font-size: 9px; fill: var(--ink-soft); letter-spacing: 0.4px; }
  .emergency-line { font-size: 19px; fill: var(--ink-soft); letter-spacing: 2.6px; }
  .brand-mark { fill: var(--brand); }
  .brand-name { font-size: 13px; font-weight: 400; fill: var(--brand); }
</style>
</head>
<body>
<svg class="lawn-sign" viewBox="0 0 846 599" xmlns="http://www.w3.org/2000/svg" preserveAspectRatio="none">
  <defs>
    <linearGradient id="accentGradient" x1="0" y1="0" x2="0" y2="1">
      <stop offset="0" stop-color="#fbee3f"/>
      <stop offset="0.45" stop-color="#faa54b"/>
      <stop offset="1" stop-color="#f26a21"/>
    </linearGradient>
    <linearGradient id="badgeGradient" x1="0" y1="0" x2="0" y2="1">
      <stop offset="0" stop-color="#86cfc6"/>
      <stop offset="1" stop-color="#4fc07a"/>
    </linearGradient>
    <linearGradient id="gutterPhotoA" x1="0" y1="0" x2="1" y2="1">
      <stop offset="0" stop-color="#dfeee6"/>
      <stop offset="0.45" stop-color="#7fb6ad"/>
      <stop offset="1" stop-color="#2f6a73"/>
    </linearGradient>
    <linearGradient id="gutterPhotoB" x1="0" y1="0" x2="1" y2="1">
      <stop offset="0" stop-color="#d8e58a"/>
      <stop offset="0.5" stop-color="#8fae7c"/>
      <stop offset="1" stop-color="#3f5e5c"/>
    </linearGradient>
    <linearGradient id="installerPhoto" x1="0" y1="0" x2="0" y2="1">
      <stop offset="0" stop-color="#e6f0ea"/>
      <stop offset="0.5" stop-color="#a9c98a"/>
      <stop offset="1" stop-color="#d6e6cf"/>
    </linearGradient>
  </defs>

  <g class="background-geometry">
    <line class="guide-line" x1="0" y1="445" x2="445" y2="0"/>
    <line class="guide-line" x1="290" y1="290" x2="600" y2="599"/>
    <line class="guide-line" x1="700" y1="0" x2="846" y2="146"/>
    <line class="guide-line" x1="846" y1="210" x2="760" y2="296"/>
  </g>

  <g class="accent-tiles">
    <rect class="accent-tile" x="259.5" y="-60.5" width="141" height="141" rx="18" transform="rotate(45 330 10)"/>
    <rect class="accent-tile" x="-70" y="165" width="120" height="120" rx="16" transform="rotate(45 -10 225)"/>
    <rect class="accent-tile" x="442" y="337" width="116" height="116" rx="16" transform="rotate(45 500 395)"/>
  </g>

  <g class="photo-tiles">
    <rect role="img" aria-label="Photo of a white gutter downspout on blue house siding"
          x="64" y="14" width="212" height="212" rx="22" fill="url(#gutterPhotoA)"
          transform="rotate(45 170 120)"/>
    <rect role="img" aria-label="Photo of a gutter and downspout beside a shingled roof"
          x="413" y="-32" width="304" height="304" rx="26" fill="url(#gutterPhotoB)"
          transform="rotate(45 565 120)"/>
    <rect role="img" aria-label="Photo of a worker in a hard hat installing a gutter under a roof edge"
          class="tile-frame" x="227.5" y="187.5" width="209" height="209" rx="22" fill="url(#installerPhoto)"
          transform="rotate(45 332 292)"/>
  </g>

  <g class="warranty">
    <text class="warranty-figure" x="708" y="362" text-anchor="middle">30-50</text>
    <text class="warranty-label" x="708" y="401" text-anchor="middle">YEAR WARRANTIES</text>
  </g>

  <g class="services">
    <g class="service service--windows">
      <circle class="service-badge" cx="613" cy="462" r="28"/>
      <rect class="service-glyph" x="598" y="447" width="13.5" height="13.5" rx="3"/>
      <rect class="service-glyph" x="614.5" y="447" width="13.5" height="13.5" rx="3"/>
      <rect class="service-glyph" x="598" y="463.5" width="13.5" height="13.5" rx="3"/>
      <rect class="service-glyph" x="614.5" y="463.5" width="13.5" height="13.5" rx="3"/>
      <text class="service-label" x="613" y="508" text-anchor="middle">WINDOWS</text>
    </g>
    <g class="service service--roofing">
      <circle class="service-badge" cx="703" cy="462" r="28"/>
      <path class="service-glyph" d="M703 444 L722 458 L718 462 L718 478 L688 478 L688 462 L684 458 Z"/>
      <rect x="697" y="462" width="4" height="4" fill="#6cc8a0"/>
      <rect x="705" y="462" width="4" height="4" fill="#6cc8a0"/>
      <text class="service-label" x="703" y="508" text-anchor="middle">ROOFING</text>
    </g>
    <g class="service service--gutters">
      <circle class="service-badge" cx="790" cy="462" r="28"/>
      <circle cx="786" cy="458" r="9" fill="none" stroke="#ffffff" stroke-width="4"/>
      <line x1="793" y1="465" x2="802" y2="474" stroke="#ffffff" stroke-width="5" stroke-linecap="round"/>
      <text class="service-label" x="790" y="508" text-anchor="middle">GUTTERS</text>
    </g>
  </g>

  <text class="emergency-line" x="627" y="559" text-anchor="middle">EMERGENCY SERVICES AVAILABLE</text>

  <g class="brand">
    <circle class="brand-mark" cx="128" cy="492" r="16"/>
    <text class="brand-name" x="180" y="516">MARLOWE</text>
    <text class="brand-name" x="180" y="532">Renewal</text>
    <text class="brand-name" x="180" y="548">Home Exteriors Co.</text>
  </g>
</svg>
</body>
</html>
```